Graphic Design Project

We make rose petal jelly from old fashioned english roses. The jelly is sweet eaten with scones and clotted cream or as a filling in a victoria sandwich, as a topping on ice cream or thick set yogurt.
The image of the product is luxurious and decadent and very english.
We need a design for a label which has a picture of an old fashioned rose (rosa mundi or a compte de chambard) The rose must stand out clearly so the jelly is not confused with other fruit jams. The overall colour of the label should be pink and soft, with white or dark pink writing. The label needs to be fridge proof.

We also need a security strip to fit on the lid of the jar.

We need the following information on the label.
Name of our company-"Petal Lantern"
Name of Product-"Rose Petal Jelly"
Sales pitch-"With whole petals-a taste of summer, delicious on scones, as a filling in sponge cake, as a topping on ice cream or yogurt."
INGREDIENTS: Sugar, water, rose petals, lemon juice, natural jelling agent (agar-agar)
STORAGE: Store in a cool dry place, once opened keep refrigerated and consume within 4 weeks.
BEST BEFORE: See base

200g
Produced by:
PETAL LANTERN
The Brambles
Marsh Lane
Ashcombe
Gloucestershire
GL19 4QT
The label must have room for a bar code. The size of label approx 8-10cm long 5cm wide.
Updates

Hi

Just been looking at the Greville and Hartley site and the labels they have there have the up market feel I am trying to convey. Hope that helps, its classy but not twee.

Thanks

Thanks for all submissions. I would be grateful if you googled images for 'Colourful and expensive biscuits at Greville Hartley' The designs on the tins are the image we are trying to create. The colours are quite strong.

Thanks

Target Market(s)

older well off people who visit garden centres

Industry/Entity Type

Security

Requirements
Must have
• All writen info above and picture of old fashioned rose prferably rose a mundi. Luxury feel, very english, to appeal to older market
Pink colour sheme
Should not have
• dark or manly colours

```html
<!DOCTYPE html>
<html lang="en">
<head>
<meta charset="utf-8">
<title>Petal Lantern – Rose Petal Jelly Label</title>
<link rel="stylesheet" href="https://fonts.googleapis.com/css2?family=Arimo:wght@400;700&family=Crimson+Pro:ital,wght@0,400;1,400&family=Marcellus+SC&display=swap">
<style>
  :root {
    --rose-pink: #db5f98;
    --rose-text: #d35c95;
    --cream-light: #fffdf7;
    --cream-warm: #fbf1dc;
    --white: #ffffff;
    --ink: #1a1a1a;
    --bloom-deep: #e98fb0;
    --bloom-soft: #f7d3de;
    --leaf: #b9c89a;
  }
  * { margin: 0; padding: 0; box-sizing: border-box; }
  html, body {
    width: 1200px; height: 666px; overflow: hidden;
    background: var(--white);
  }
  .label {
    position: relative; width: 1200px; height: 666px; overflow: hidden;
    background: linear-gradient(90deg, var(--cream-light) 0%, var(--cream-light) 35%, var(--cream-warm) 100%);
    font-family: "Arimo", Arial, sans-serif;
  }
  .brand-tab {
    position: absolute; left: 350px; top: 0; width: 497px; height: 87px;
    background: var(--rose-pink);
    border-radius: 0 0 34px 34px;
    display: flex; align-items: center; justify-content: center;
    font-family: "Marcellus SC", serif;
    font-size: 36px; letter-spacing: 3px;
    color: var(--cream-light);
    padding-top: 4px;
  }
  .rose-art {
    position: absolute; left: 0; top: 0; width: 294px; height: 480px;
    background:
      radial-gradient(ellipse 60% 35% at 30% 28%, var(--bloom-deep) 0%, transparent 70%),
      radial-gradient(ellipse 55% 30% at 60% 62%, var(--bloom-soft) 0%, transparent 75%),
      radial-gradient(ellipse 50% 25% at 25% 88%, var(--bloom-deep) 0%, transparent 70%),
      linear-gradient(180deg, #f3c2d2 0%, #f6d8e1 50%, #f0bccd 100%);
    -webkit-mask-image: linear-gradient(90deg, #000 75%, transparent 100%);
            mask-image: linear-gradient(90deg, #000 75%, transparent 100%);
  }
  .product-name {
    position: absolute; left: 230px; width: 750px; top: 118px;
    text-align: center;
    font-family: "Crimson Pro", "Times New Roman", serif;
    font-weight: 400; font-size: 100px; line-height: 1;
    color: var(--rose-text);
  }
  .sales-pitch {
    position: absolute; left: 280px; width: 696px; top: 268px;
    text-align: center;
    font-family: "Crimson Pro", "Times New Roman", serif;
    font-style: italic; font-size: 32px; line-height: 47px;
    color: var(--rose-text);
  }
  .net-weight {
    position: absolute; left: 504px; width: 200px; top: 442px;
    text-align: center; font-size: 24px; color: var(--rose-text);
  }
  .producer-address {
    position: absolute; left: 1008px; top: 372px;
    transform: rotate(-90deg); transform-origin: 0 0;
    width: 345px;
    font-size: 25px; line-height: 38px; color: var(--rose-text);
    white-space: nowrap;
  }
  .divider-line {
    position: absolute; left: 0; top: 478px; width: 1200px; height: 6px;
    background: var(--rose-pink);
  }
  .info-band {
    position: absolute; left: 0; top: 496px; width: 1200px; height: 170px;
    background: var(--rose-pink);
  }
  .product-facts {
    position: absolute; left: 34px; top: 514px; width: 700px;
    font-weight: 700; font-size: 21.5px; line-height: 32px;
    color: var(--white);
  }
  .best-before {
    position: absolute; right: 233px; top: 565px;
    text-align: right;
    font-weight: 700; font-size: 21.5px; line-height: 30px;
    color: var(--white);
  }
  .barcode-area {
    position: absolute; left: 992px; top: 400px; width: 181px; height: 237px;
    background: var(--white);
    border: 1.5px solid #8a8a8a;
    display: flex; align-items: center; justify-content: center;
  }
  .barcode-area span {
    transform: rotate(-90deg);
    font-size: 30px; line-height: 36px; text-align: center;
    color: var(--ink); white-space: nowrap;
  }
</style>
</head>
<body>
  <div class="label">
    <div class="rose-art" role="img" aria-label="Illustration of old fashioned pink English roses with buds and leaves"></div>

    <header class="brand-tab">Petal Lantern</header>

    <h1 class="product-name">Rose Petal Jelly</h1>

    <p class="sales-pitch">With whole petals - a taste of summer, delicious<br>on scones, as a filling in sponge cake,<br>as a topping on ice cream or yogurt.</p>

    <p class="net-weight">200g</p>

    <address class="producer-address" style="font-style:normal">
      PETAL LANTERN<br>
      The Brambles, Marsh Lane,<br>
      Ashcombe, Gloucestershire<br>
      GL19 4QT
    </address>

    <div class="divider-line"></div>
    <div class="info-band"></div>

    <div class="product-facts">
      INGREDIENTS: Sugar, water, rose petals, lemon juice,<br>
      natural jelling agent (agar-agar)<br>
      STORAGE: Store in a cool dry place, once opened keep<br>
      refrigerated and consume within 4 weeks.
    </div>

    <div class="best-before">BEST BEFORE:<br>See base</div>

    <div class="barcode-area"><span>BAR<br>CODE</span></div>
  </div>
</body>
</html>
```